Webdesign für Wandertouren
Hi Wenke, thank you very much for the wonderful and successful collaboration. I was very pleased that you contributed your ideas so well. I'm really happy with your design and I'm looking forward to the reactions of my guests. I wish you many great clients and a lot of success in the future. Best regards Rieke
Zielgruppe
Liebe Designende, wunderbar, dass Du hier gelandet bist.
Ich biete als International Mountain Leader
Wandertouren, Trekkingreisen und Naturerlebnisse - regional und international an. Die Touren werden (noch alle) von mir persönlich durchgeführt.
Hier der Einstiegstext für die Startseite.
Atemberaubende Landschaften mit majestätischen Bergen, wunderschönen Hochebenen und beeindruckenden Wasserfällen verzaubern Deine Seele.
Wandertouren, Trekkingreisen und Naturerlebnisse führen Dich in fantastische Paradieswelten. Hier erlebst Du eindrucksvolle Glücksgefühle. Gerührt von der Schönheit und der Einzigartigkeit der wundervollen Natur kannst Du Dich tief entspannen und die Gegenwart genießen.
On Top gibt es dazu urige Berghütten und inspirierende Begegnungen, die Deine Gipfelpfade zu wundervollen Erlebnissen für Dich machen.
Und hast Du schon Lust bekommen mitzukommen?
Zielgruppe: Frauen und Männer zwischen 38 - 65 Jahren
Aufgabenstellung
*Ich liebe den Hintergrund mit altem Holz, dazu schicke ich Bilder mit. Mehr kann ich dann noch im Verlauf des Projektes schicken, da ich nur 10 Bilder auf einmal hochladen kann.
*Ich schicke Bilder aus einem Smoothie Rezept Buch, JPG 5465 das finde ich witzig um die Seite aufzulockern, vielleicht gibt es ja Ideen dazu wie es umgesetzt werden kann. - Dementsprechend möchte ich diese Elemente auch in dem Flyerprojekt im Anschluß umgesetzt haben.
Kräftige Farben sind gewünscht. Pink ist eh in meinem Logo. Gerne auch ein helles Lindgrün.

```html
<!DOCTYPE html>
<html lang="de">
<head>
<meta charset="utf-8">
<title>Gipfelpfade – Wandertouren</title>
<link rel="stylesheet" href="https://fonts.googleapis.com/css2?family=Barlow:wght@400;500;600&family=Permanent+Marker&display=swap">
<style>
:root{
  --pink:#e2136b;
  --green:#9cc954;
  --dark:#2b2626;
  --wood-dark:#4a2c18;
  --wood-mid:#7a4d2c;
  --wood-light:#9a6a42;
  --white:#ffffff;
  --stage:#f4f4f4;
}
*{margin:0;padding:0;box-sizing:border-box}
html,body{width:1200px;height:1200px;overflow:hidden;background:var(--stage);font-family:"Barlow",sans-serif}
.page{position:absolute;left:262px;top:30px;width:1040px;height:1757px;transform:scale(0.649);transform-origin:0 0;background:var(--white);overflow:hidden}
.nav{position:absolute;left:0;top:0;width:1040px;height:53px;background:var(--pink);color:var(--white);font-size:13px;font-weight:500}
.nav-item{position:absolute;top:18px}
.nav-item.is-active{border-left:2px solid var(--white);padding-left:7px;left:62px;top:14px;padding-top:4px;padding-bottom:4px}
.nav-phone{display:block;font-size:9px;font-weight:400;margin-top:1px}
.nav-burger{position:absolute;left:978px;top:16px;width:29px;height:20px}
.nav-burger span{display:block;height:3px;background:var(--white);margin-bottom:5px;border-radius:2px}
.hero{position:absolute;left:0;top:53px;width:1040px;height:532px;overflow:hidden}
.hero svg{position:absolute;left:0;top:0}
.brand{position:absolute;left:70px;top:150px;width:240px;text-align:center}
.brand-mark{width:60px;height:60px;border-radius:50%;background:var(--pink);margin:0 auto 40px}
.brand-name{font-size:40px;font-weight:600;color:var(--dark);line-height:1}
.brand-sub{font-size:14px;font-weight:600;color:var(--dark);letter-spacing:3px;margin-top:10px}
.social{position:absolute;left:30px;top:485px;display:flex;gap:8px}
.social span{width:24px;height:24px;border-radius:50%;background:var(--pink)}
.polaroid{position:absolute;background:var(--white);padding:12px;box-shadow:0 4px 10px rgba(0,0,0,.45)}
.polaroid .photo{width:100%;height:100%}
.caption{position:absolute;font-family:"Permanent Marker",sans-serif;color:var(--white);font-size:11px;white-space:nowrap;line-height:1}
.to-top{position:absolute;left:968px;top:472px;width:46px;height:46px;border-radius:50%;background:var(--pink)}
.band{position:absolute;left:0;top:585px;width:1040px;height:22px;background:var(--dark)}
.tours{position:absolute;left:0;top:607px;width:1040px;height:565px;background:var(--white)}
.tours svg{position:absolute;left:0;top:0}
.section-title{font-family:"Permanent Marker",sans-serif;font-size:30px;letter-spacing:1px;font-weight:400;line-height:1}
.tours .section-title{position:absolute;left:82px;top:55px;color:var(--green)}
.rule{position:absolute;height:2px}
.tours-copy{position:absolute;left:82px;top:134px;width:343px;font-size:12px;line-height:15px;color:#1c1c1c;text-align:justify;hyphens:auto}
.tours-copy h3{font-size:14.5px;font-weight:600;line-height:18px;margin:18px 0 6px;text-align:left}
.contact{position:absolute;left:0;top:1172px;width:1040px;height:585px;background:linear-gradient(180deg,var(--wood-mid) 0%,var(--wood-light) 30%,var(--wood-mid) 60%,var(--wood-dark) 100%)}
.contact .section-title{position:absolute;left:145px;top:70px;color:var(--white);font-size:26px}
.contact-intro{position:absolute;left:142px;top:128px;color:var(--white);font-size:14px;font-weight:500}
.field{position:absolute;background:var(--green);border-radius:10px;color:var(--white);font-size:18px;font-weight:500;padding:12px 22px}
.submit{position:absolute;left:147px;top:369px;width:166px;height:38px;border-radius:19px;background:var(--green);color:var(--white);font-size:13px;font-weight:500;text-align:center;line-height:38px}
.footer-col{position:absolute;top:474px;color:var(--white);font-size:16px;line-height:20px}
.footer-col.small{font-size:13px;line-height:17px}
</style>
</head>
<body>
<div class="page">
  <nav class="nav">
    <span class="nav-item is-active">Startseite</span>
    <span class="nav-item" style="left:191px">Wandertouren</span>
    <span class="nav-item" style="left:341px">Trekkingreisen</span>
    <span class="nav-item" style="left:488px">Naturerlebnisse</span>
    <span class="nav-item" style="left:644px">Deine Guide Rieke</span>
    <span class="nav-item" style="left:805px;top:13px">Kontakt<span class="nav-phone">+49 (0)1500 11 222 33</span></span>
    <div class="nav-burger"><span></span><span></span><span></span></div>
  </nav>

  <section class="hero">
    <svg width="1040" height="532" viewBox="0 0 1040 532">
      <defs>
        <linearGradient id="woodTone" x1="0" y1="0" x2="0" y2="1">
          <stop offset="0" stop-color="#8a5a34"/>
          <stop offset=".5" stop-color="#6e4326"/>
          <stop offset="1" stop-color="#4a2c18"/>
        </linearGradient>
      </defs>
      <rect width="1040" height="532" fill="url(#woodTone)" role="img" aria-label="Holzbrett-Hintergrund aus altem Holz"/>
      <path d="M0 0H400C420 40 450 80 450 150C450 230 420 260 380 300C300 350 260 400 255 532H0Z" fill="var(--white)"/>
      <path d="M0 0H258C240 40 200 70 120 90C60 110 60 150 55 200C50 240 20 250 0 255Z" fill="var(--pink)"/>
      <path d="M0 0H190C170 30 130 50 70 70C40 85 25 110 20 150C15 190 8 200 0 205Z" fill="var(--dark)"/>
      <path d="M908 0H1040V170C1025 150 1020 120 1000 100C980 80 950 75 925 55C905 40 900 15 908 0Z" fill="var(--green)"/>
    </svg>
    <div class="brand">
      <div class="brand-mark"></div>
      <div class="brand-name">Gipfelpfade</div>
      <div class="brand-sub">RIEKE SOLWALD</div>
    </div>
    <div class="social"><span></span><span></span><span></span></div>

    <div class="polaroid" style="left:472px;top:33px;width:243px;height:245px;transform:rotate(-2deg)">
      <div class="photo" role="img" aria-label="Foto: Bergführerin vor Felsgipfel" style="background:linear-gradient(160deg,#a9b8c8,#8c95a0 55%,#3c3d3a)"></div>
    </div>
    <div class="polaroid" style="left:660px;top:105px;width:340px;height:335px;transform:rotate(3deg)">
      <div class="photo" role="img" aria-label="Foto: Wanderschuhe über einem Gebirgstal" style="background:linear-gradient(170deg,#b9bcb7,#9ea39a 45%,#6d6456 80%,#4b4036)"></div>
    </div>
    <div class="polaroid" style="left:355px;top:272px;width:245px;height:228px;transform:rotate(-12deg)">
      <div class="photo" role="img" aria-label="Foto: zwei Wanderinnen jubeln auf einem Gipfelfelsen" style="background:linear-gradient(180deg,#5f9ad8,#9cc4ea 60%,#6f6a60)"></div>
    </div>
    <span class="caption" style="left:558px;top:54px;font-size:10px;transform:rotate(-2deg)">GIPFELGLÜCK GENIESSEN!</span>
    <span class="caption" style="left:764px;top:86px;transform:rotate(3deg)">VERZAUBERN LASSEN!</span>
    <span class="caption" style="left:720px;top:450px;transform:rotate(4deg)">GEMEINSAM UNTERWEGS SEIN!</span>
    <span class="caption" style="left:405px;top:478px;transform:rotate(-12deg)">GIPFELPFADE ERLEBEN!</span>
    <div class="to-top">
      <svg width="46" height="46" viewBox="0 0 46 46"><path d="M23 11L33 24H26V36H20V24H13Z" fill="var(--white)"/></svg>
    </div>
  </section>

  <div class="band"></div>

  <section class="tours">
    <svg width="1040" height="565" viewBox="0 0 1040 565">
      <path d="M0 378C30 370 55 395 55 430C58 460 80 470 110 465C160 458 190 480 200 510C205 535 215 550 225 565H0Z" fill="var(--green)"/>
      <path d="M500 0H1040V555C990 560 930 545 870 525C830 510 790 530 760 540C720 550 690 530 640 520C560 505 495 480 480 400C470 340 500 320 540 280C570 240 540 200 510 160C485 120 480 40 500 0Z" fill="var(--pink)"/>
      <path d="M545 0H1040V520C990 525 930 510 880 495C840 485 805 500 780 505C740 512 700 495 650 485C585 470 545 450 545 400C545 350 565 330 580 300C595 260 570 220 555 190C540 160 535 90 545 0Z" fill="#5a97d6" role="img" aria-label="Foto: Wandergruppe jubelt mit Stöcken auf einem Gipfel"/>
      <path d="M545 300H1040V520C990 525 930 510 880 495C840 485 805 500 780 505C740 512 700 495 650 485C585 470 545 450 545 400Z" fill="#7a8a5a" opacity=".55"/>
    </svg>
    <h2 class="section-title">WANDERTOUREN</h2>
    <div class="rule" style="left:82px;top:98px;width:133px;background:var(--green)"></div>
    <div class="tours-copy">
      <p>Wir sind Spezialisten für Personalentwicklung in Unternehmen. Mitarbeiter zählen zum wertvollsten Kapital eines Unternehmens. Sie sind Träger des Firmen-Know-hows, treiben Ideen voran und sind für die Qualität von Produkten und Dienstleistungen verantwortlich. Damit Ihre Mitarbeiter ihre Ressourcen voll ausschöpfen können, brauchen sie klare Ziele, Vertrauen in Ihre Führungskräfte und Unterstützung durch ihre Kollegen.</p>
      <h3>Wir stärken gegenseitiges Vertrauen<br>und entwickeln großartige Teams</h3>
      <p>Unsere Naturcoachings und Trainings stärken das gegenseitige Vertrauen und bringen neue Ressourcen zum Vorschein. Sie verbinden die Menschen zu großartigen Teams und motivieren zur Umsetzung der neuen Erkenntnisse mit konkreten Handlungsstrategien die Spaß machen.</p>
    </div>
  </section>

  <section class="contact" role="img" aria-label="Holzbrett-Hintergrund aus altem Holz">
    <h2 class="section-title">KONTAKT</h2>
    <div class="rule" style="left:145px;top:108px;width:70px;background:var(--white)"></div>
    <p class="contact-intro">Bitte füllen Sie dieses Formular vollständig aus.</p>
    <div class="field" style="left:141px;top:161px;width:247px;height:47px">E-Mail</div>
    <div class="field" style="left:422px;top:161px;width:247px;height:47px">Telefonnummer</div>
    <div class="field" style="left:143px;top:220px;width:757px;height:120px">Ihre Nachricht...</div>
    <div class="submit">Abschicken!</div>
    <div class="rule" style="left:128px;top:444px;width:870px;background:var(--white)"></div>
    <div class="footer-col" style="left:128px">Musterfirma<br>Musterstraße 20,<br>12555 Stadt</div>
    <div class="footer-col" style="left:345px">Tel: +49 (0)30 000 111 22<br>mail@muster.de</div>
    <div class="footer-col small" style="left:618px">Inhaber:<br>Max Mustermann</div>
  </section>
</div>
</body>
</html>
```